Harbor Circuits LLC is a Minneapolis / St Paul and surrounding communities computer repair and service company. It serves residential and small businesses. We work primarily with virus removal, data recovery, system baselines, networking, and new system installation. The site should look clean, professional, and easy to navigate.

This wordpress project must be coded and integrated into a wordpress theme for easy upload and maintenance.
Updates

Designers - Please make sure your design is in a wordpress theme so that It can be uploaded.  

Thank you,

Brent 

Target Market(s)

Residential and Small Business

Industry/Entity Type

Residential

Requirements
Must have
• Site Content
1. Main Page should have photos that scroll across, Business Description, Space to run
“Specials” Ads
a. Intuitive Navigation
2. Additional Pages
a. Blog for Computer Repair Articles
b. Testimonials Page
c. Contact Pages
d. Services Page with the ability to put in pricing
3. The site must be clean and professional.
4. Wordpress Theme

```html
<!DOCTYPE html>
<html lang="en">
<head>
<meta charset="utf-8">
<title>Blog – Harbor Circuits LLC</title>
<link href="https://fonts.googleapis.com/css2?family=Montserrat:wght@400;500;600;700&family=Noto+Serif:wght@400&family=Open+Sans:wght@400;600&display=swap" rel="stylesheet">
<style>
:root{
  --page:#dfe2d7;
  --band:#3b3b3b;
  --band-dark:#2b2b2b;
  --green:#56a02a;
  --green-dark:#3f7d1d;
  --ink:#222;
  --body:#5a5a5a;
  --muted:#888;
  --rule:#e3e3e3;
  --panel:#f2f2f2;
  --footer:#2e3436;
  --footer-text:#c9cdce;
  --ad-red:#d22a30;
  --ad-blue:#1f4e9c;
}
*{box-sizing:border-box;margin:0;padding:0}
html,body{width:889px;height:1200px;overflow:hidden}
body{position:relative;background:var(--page);font-family:"Open Sans",Arial,sans-serif;color:var(--ink)}
.nav-band{position:absolute;left:0;top:72px;width:889px;height:90px;background:linear-gradient(var(--band-dark),var(--band))}
.brand{position:absolute;left:105px;top:8px;display:flex;align-items:center;gap:10px}
.brand-mark{width:52px;height:52px;border:3px solid var(--green);border-radius:50%}
.brand-name{font-family:"Montserrat",sans-serif;font-weight:600;font-size:20px;color:#4a4a4a}
.contact-top{position:absolute;left:555px;top:22px;font-family:"Montserrat",sans-serif}
.contact-top div{display:flex;align-items:center;gap:10px}
.phone{font-size:15px;color:#333}
.email{margin-top:10px;font-size:10.5px;color:var(--green-dark)}
.main-nav{position:absolute;left:110px;top:83px;display:flex;gap:17px;font-family:"Montserrat",sans-serif;font-weight:500;font-size:12px;color:#fff}
.search{position:absolute;left:588px;top:83px;width:191px;height:18px;background:#fff;border-radius:9px;overflow:hidden;display:flex}
.search svg{margin:4px 0 0 6px}
.search-btn{margin-left:auto;width:46px;background:linear-gradient(#f4f4f4,#d9d9d9);font-size:9.5px;font-weight:600;text-align:center;line-height:18px;color:#333;border-left:1px solid #ccc}
.sheet{position:absolute;left:97px;top:110px;width:694px;height:968px;background:#fff;border-radius:4px 4px 0 0}
.hero{position:absolute;left:104px;top:118px;width:680px;height:162px;border:1px solid #ddd;border-radius:3px;padding:3px}
.hero-art{height:109px;background:linear-gradient(100deg,#1b3d78,#4f86c4 40%,#1a3766 75%,#0d2347);position:relative}
.hero-line{position:absolute;left:420px;font-family:"Montserrat",sans-serif;color:#fff;text-transform:uppercase;letter-spacing:-.5px}
.hero-bar{height:46px;background:var(--green);color:#fff;font-family:"Montserrat",sans-serif;font-weight:500;font-size:17px;padding:12px 14px}
.section-title{position:absolute;left:118px;top:292px;width:418px;font-family:"Montserrat",sans-serif;font-weight:500;font-size:11.5px;padding-bottom:6px;border-bottom:1px solid var(--rule)}
.post{position:absolute;left:111px;width:426px}
.date{position:absolute;left:0;top:0;width:46px;height:40px;background:var(--green);color:#fff;text-align:center;font-family:"Montserrat",sans-serif;font-weight:600;line-height:1}
.date::after{content:"";position:absolute;left:0;bottom:-6px;border-top:6px solid var(--green-dark);border-left:6px solid transparent}
.date .m{font-size:8.5px;display:block;padding-top:3px}
.date .d{font-size:14px;display:block}
.date .y{font-size:8px;display:block}
.post-body{margin-left:53px}
.post-title{font-family:"Noto Serif",serif;font-size:13.5px;font-weight:400;color:#111;padding-top:4px}
.byline{font-size:8px;color:var(--muted)}
.byline a{color:var(--green-dark);text-decoration:none}
.excerpt{margin-top:10px;font-size:8.9px;line-height:13.9px;color:var(--body)}
.post-meta{margin-top:6px;border-top:1px solid #eee;border-bottom:1px solid #eee;height:21px;display:flex;justify-content:space-between;align-items:center;font-size:9.5px;color:var(--green-dark)}
.post-meta span{display:flex;align-items:center;gap:5px}
.sidebar{position:absolute;left:551px;top:301px;width:227px;height:610px;background:var(--panel);border:1px solid #e0e0e0;border-radius:3px}
.ad{position:absolute;left:9px;top:8px;width:209px;height:173px;border:4px solid var(--ad-red);background:#f5f5f5;text-align:center;font-family:"Montserrat",sans-serif}
.ad-head{color:var(--ad-red);font-weight:700;font-size:22px;line-height:30px;margin-top:8px}
.ad-box{width:174px;height:36px;margin:8px auto 0;background:var(--ad-blue);border-radius:4px;color:#fff;font-weight:700;font-size:18px;line-height:36px}
.ad-sub{color:var(--ad-blue);font-weight:700;font-style:italic;font-size:12.5px;margin-top:3px}
.ad-price{color:var(--ad-red);font-style:italic;font-size:12px;font-weight:600}
.widget-head{position:absolute;left:9px;width:209px;height:26px;background:var(--green);border-radius:4px 4px 0 0;color:#fff;font-family:"Montserrat",sans-serif;font-weight:500;font-size:11.5px;padding:6px 10px}
.topics{position:absolute;left:19px;top:228px;list-style:none;font-size:9px;color:#555}
.topics li{height:17.3px;padding-left:10px;position:relative}
.topics li::before{content:"";position:absolute;left:0;top:4px;border-left:3px solid #999;border-top:2.5px solid transparent;border-bottom:2.5px solid transparent}
.recent{position:absolute;left:9px;top:440px;width:209px;list-style:none;font-family:"Montserrat",sans-serif;font-size:11px;color:#666}
.recent li{height:31.3px;padding:9px 10px 0;border-bottom:1px solid #e1e1e1}
.footer{position:absolute;left:97px;top:1078px;width:694px;height:109px;background:var(--footer);color:var(--footer-text);font-size:9px;border-radius:0 0 3px 3px}
.footer h3{font-family:"Montserrat",sans-serif;font-weight:500;font-size:10px;color:#fff;margin-bottom:10px}
.fcol{position:absolute;top:10px;line-height:16px}
.fnav{display:grid;grid-template-columns:70px 70px}
.social div{display:flex;align-items:center;gap:8px;margin-bottom:5px}
.sq{width:14px;height:14px;background:#5a8fc0;border-radius:2px}
</style>
</head>
<body>
<header>
  <div class="brand"><span class="brand-mark"></span><span class="brand-name">Harbor Circuits LLC</span></div>
  <div class="contact-top">
    <div class="phone"><svg width="14" height="14" viewBox="0 0 14 14"><rect width="14" height="14" rx="2" fill="#56a02a"/><path d="M4 3l2 2-1 1.5c.6 1.2 1.3 1.9 2.5 2.5L9 8l2 2-1.5 1.5C6.5 11 3 7.5 2.5 4.5z" fill="#fff"/></svg>612-555-0148</div>
    <div class="email"><svg width="14" height="12" viewBox="0 0 14 12"><rect width="14" height="12" rx="2" fill="#56a02a"/><path d="M2 3l5 4 5-4" stroke="#fff" stroke-width="1.5" fill="none"/></svg>CustomerService@HarborCircuitsLLC.com</div>
  </div>
</header>
<div class="nav-band"></div>
<nav class="main-nav"><span>Home</span><span>About Us</span><span>Services</span><span>Products</span><span>Blog</span><span>Testimonials</span><span>Contact Us</span></nav>
<div class="search"><svg width="10" height="10" viewBox="0 0 10 10"><circle cx="4" cy="4" r="3" stroke="#777" stroke-width="1.5" fill="none"/><path d="M6 6l3 3" stroke="#777" stroke-width="1.5"/></svg><span class="search-btn">Search</span></div>

<main class="sheet"></main>
<section class="hero">
  <div class="hero-art" role="img" aria-label="Close-up photograph of a blue circuit board">
    <div class="hero-line" style="top:48px;font-weight:700;font-size:26px">Lorem Ipsum</div>
    <div class="hero-line" style="top:74px;font-weight:400;font-size:24px">Dolor Sit Amet</div>
  </div>
  <div class="hero-bar">Blog</div>
</section>

<h2 class="section-title">Computer Repair Blog</h2>

<article class="post" style="top:327px">
  <div class="date"><span class="m">AUG</span><span class="d">08</span><span class="y">2012</span></div>
  <div class="post-body">
    <h3 class="post-title">Nunc at diam non turpis mollis sagittis nec eget diam.</h3>
    <p class="byline">By <a href="#">Maren Holt</a></p>
    <p class="excerpt">Sed ut perspiciatis unde omnis iste natus error sit voluptatem accusantium doloremque laudantium, totam rem aperiam, eaque ipsa quae ab illo inventore veritatis et quasi architecto beatae vitae dicta sunt explicabo. Nemo enim ipsam voluptatem quia voluptas sit aspernatur aut odit aut fugit, sed quia consequuntur magni dolores eos qui ratione voluptatem sequi nesciunt. Neque porro quisquam est, qui dolorem ipsum quia dolor sit amet, consectetur, adipisci velit, sed quia non numquam eius modi tempora incidunt ut labore et dolore magnam aliquam quaerat voluptatem. Ut enim ad minima veniam, quis nostrum exercitationem ullam corporis suscipit laboriosam, nisi ut aliquid ex ea commodi consequatur? Quis autem vel eum iure reprehenderit qui in ea voluptate velit esse quam nihil molestiae consequatur, vel illum qui dolorem eum fugiat quo voluptas nulla pariatur?</p>
    <div class="post-meta"><span><svg width="12" height="10" viewBox="0 0 12 10"><ellipse cx="6" cy="4.5" rx="5" ry="3.6" fill="#8fc1e6"/><path d="M3 7l-1 3 3-2z" fill="#8fc1e6"/></svg>7 comments</span><span><svg width="12" height="10" viewBox="0 0 12 10"><path d="M1 1h4.5l.5 1 .5-1H11v8H1z" fill="none" stroke="#777"/><path d="M6 2v7" stroke="#777"/></svg>Read more</span></div>
  </div>
</article>

<article class="post" style="top:577px">
  <div class="date"><span class="m">AUG</span><span class="d">08</span><span class="y">2012</span></div>
  <div class="post-body">
    <h3 class="post-title">Nunc at diam non turpis mollis sagittis nec eget diam.</h3>
    <p class="byline">By <a href="#">Maren Holt</a></p>
    <p class="excerpt">Sed ut perspiciatis unde omnis iste natus error sit voluptatem accusantium doloremque laudantium, totam rem aperiam, eaque ipsa quae ab illo inventore veritatis et quasi architecto beatae vitae dicta sunt explicabo. Nemo enim ipsam voluptatem quia voluptas sit aspernatur aut odit aut fugit, sed quia consequuntur magni dolores eos qui ratione voluptatem sequi nesciunt. Neque porro quisquam est, qui dolorem ipsum quia dolor sit amet, consectetur, adipisci velit, sed quia non numquam eius modi tempora incidunt ut labore et dolore magnam aliquam quaerat voluptatem. Ut enim ad minima veniam, quis nostrum exercitationem ullam corporis suscipit laboriosam, nisi ut aliquid ex ea commodi consequatur? Quis autem vel eum iure reprehenderit qui in ea voluptate velit esse quam nihil molestiae consequatur, vel illum qui dolorem eum fugiat quo voluptas nulla pariatur?</p>
    <div class="post-meta"><span><svg width="12" height="10" viewBox="0 0 12 10"><ellipse cx="6" cy="4.5" rx="5" ry="3.6" fill="#8fc1e6"/><path d="M3 7l-1 3 3-2z" fill="#8fc1e6"/></svg>7 comments</span><span><svg width="12" height="10" viewBox="0 0 12 10"><path d="M1 1h4.5l.5 1 .5-1H11v8H1z" fill="none" stroke="#777"/><path d="M6 2v7" stroke="#777"/></svg>Read more</span></div>
  </div>
</article>

<article class="post" style="top:825px">
  <div class="date"><span class="m">AUG</span><span class="d">08</span><span class="y">2012</span></div>
  <div class="post-body">
    <h3 class="post-title">Nunc at diam non turpis mollis sagittis nec eget diam.</h3>
    <p class="byline">By <a href="#">Maren Holt</a></p>
    <p class="excerpt">Sed ut perspiciatis unde omnis iste natus error sit voluptatem accusantium doloremque laudantium, totam rem aperiam, eaque ipsa quae ab illo inventore veritatis et quasi architecto beatae vitae dicta sunt explicabo. Nemo enim ipsam voluptatem quia voluptas sit aspernatur aut odit aut fugit, sed quia consequuntur magni dolores eos qui ratione voluptatem sequi nesciunt. Neque porro quisquam est, qui dolorem ipsum quia dolor sit amet, consectetur, adipisci velit, sed quia non numquam eius modi tempora incidunt ut labore et dolore magnam aliquam quaerat voluptatem. Ut enim ad minima veniam, quis nostrum exercitationem ullam corporis suscipit laboriosam, nisi ut aliquid ex ea commodi consequatur? Quis autem vel eum iure reprehenderit qui in ea voluptate velit esse quam nihil molestiae consequatur, vel illum qui dolorem eum fugiat quo voluptas nulla pariatur?</p>
    <div class="post-meta"><span><svg width="12" height="10" viewBox="0 0 12 10"><ellipse cx="6" cy="4.5" rx="5" ry="3.6" fill="#8fc1e6"/><path d="M3 7l-1 3 3-2z" fill="#8fc1e6"/></svg>7 comments</span><span><svg width="12" height="10" viewBox="0 0 12 10"><path d="M1 1h4.5l.5 1 .5-1H11v8H1z" fill="none" stroke="#777"/><path d="M6 2v7" stroke="#777"/></svg>Read more</span></div>
  </div>
</article>

<aside class="sidebar">
  <div class="ad">
    <div class="ad-head">Hosted Suites<br>expensive?</div>
    <div class="ad-box">PostHarbor</div>
    <div class="ad-sub">Business Email System</div>
    <div class="ad-price">Just $1 per user /mo</div>
  </div>
  <div class="widget-head" style="top:193px">TOPICS</div>
  <ul class="topics">
    <li>Computer Security</li><li>ID Theft Protection</li><li>Internet Security</li><li>Online Privacy</li><li>Online Security &amp; Threats ABCs</li><li>Safe Social</li><li>PC Errors</li><li>Slow Computer</li><li>PC Utility Tools</li><li>Speed Up PC</li>
  </ul>
  <div class="widget-head" style="top:411px">RECENT ARTICLES</div>
  <ul class="recent">
    <li>What is Malware?</li><li>What is a Firewall?</li><li>What is Spyware?</li><li>What is Online Identity Theft?</li><li>What Are Computer Viruses?</li>
  </ul>
</aside>

<footer class="footer">
  <div class="fcol" style="left:7px"><h3>Quick Navigation</h3>
    <div class="fnav"><span>Home</span><span>Blog</span><span>About Us</span><span>Testimonials</span><span>Services</span><span>Contact Us</span><span>Products</span></div></div>
  <div class="fcol" style="left:158px"><h3>Contact Info</h3>
    <p>123 Lorem ipsum dolor<br>Some City, P.O 457845, Country</p>
    <p style="margin-top:6px;line-height:13px">P:&nbsp; 612-555-0148<br>E:&nbsp; CustomerService@HarborCircuitsLLC.com</p></div>
  <div class="fcol social" style="left:392px"><h3>Connect with us</h3>
    <div><span class="sq"></span>Join Us on Friendspace</div>
    <div><span class="sq"></span>Chirpline</div></div>
  <div class="fcol" style="left:538px"><h3>© 2012 Harbor Circuits L.L.C</h3>
    <p style="margin-top:24px;line-height:12px">All right are reserved.<br>Terms of Service | Privacy Policy</p></div>
</footer>
</body>
</html>
```